Business Card Design

I'm looking for a cool business card design that showcases what my company does... I am the owner and Brava is a play on my last name. The Brava Group is a privately held entity that specializes in media (Brava Media) and financial services (Brava Trading).

Brava Media focuses on the distribution and management of quality entertainment properties to all areas of the media world including broadcast, cable, digital, mobile and social media. Brava Media helps media and entertainment companies create and market great content and ensure that it reaches the widest audience possible.

Brava Media currently represents Ripple TV (www.rippletv-example.com), the fastest growing over the air broadcast network that focuses on programming that appeals to the African American audience. Brava Media also represents two new over the air broadcast networks launching in Summer 2014 - Harbor TV (www.harbortv-example.com) and Maple TV (www.mapletv-example.com).

Brava Media is an investor and business partner in SunDrift (www.sundrift-example.com) - a mobile social platform that empowers the user to choose how long your photos and videos live online.

Brava Media also represents KRN Enterprises (www.krnent-example.com), an independent producer that creates talent-driven and cost-effective programming around emerging talent and Clearbrook Content, a prolific producer of multimedia content including QXN's hit program - Velvet Hall.

Brava Trading manages a family office and focuses on building meaningful partnerships with all major financial institutions with a heavy concentration on IPO and secondary offerings.

Industry/Entity Type

Entertainment

Contact Information for Business Card

Martin Hale
12 Cobalt Lane
Roslyn New York 11492
O 516.555.0143
C 516.555.0178

```html
<!DOCTYPE html>
<html lang="en">
<head>
<meta charset="utf-8">
<title>The Brava Group – Business Card</title>
<link rel="stylesheet" href="https://fonts.googleapis.com/css2?family=Open+Sans:wght@400;700&display=swap">
<style>
  :root {
    --backdrop: #e8e5e0;
    --charcoal: #4b4c4e;
    --charcoal-deep: #3e3f41;
    --scene-grey: #6a6b6d;
    --paper: #ffffff;
    --paper-shade: #ececec;
    --amber: #e6a23c;
    --ink: #3a3b3d;
    --moon: #efe6c2;
  }
  * { box-sizing: border-box; margin: 0; padding: 0; }
  html, body {
    width: 1200px; height: 1023px; overflow: hidden;
    background: var(--backdrop);
    font-family: "Open Sans", Arial, sans-serif;
  }
  .card {
    position: absolute; left: 110px; top: 231px;
    width: 980px; height: 560px;
    background: var(--paper);
    box-shadow: 0 10px 30px rgba(0,0,0,.25);
    overflow: hidden;
  }
  .card__header {
    position: absolute; left: 0; top: 0; width: 100%; height: 170px;
    background: linear-gradient(180deg, var(--charcoal) 0%, var(--charcoal-deep) 100%);
  }
  .brand {
    position: absolute; left: 40px; top: 35px;
    display: flex; align-items: center; gap: 26px;
  }
  .brand__disc {
    width: 100px; height: 100px; border-radius: 50%;
    background: var(--moon);
  }
  .brand__name {
    color: var(--amber); font-weight: 700; font-size: 58px;
    letter-spacing: 1px; line-height: 1;
  }
  .card__body {
    position: absolute; left: 0; top: 170px; width: 100%; height: 320px;
    background: linear-gradient(180deg, var(--paper) 0%, var(--paper-shade) 100%);
  }
  .scenery {
    position: absolute; right: 0; top: 0; width: 300px; height: 320px;
    background: linear-gradient(90deg, var(--paper-shade) 0%, var(--scene-grey) 100%);
  }
  .contact {
    position: absolute; left: 60px; top: 40px;
  }
  .contact__name {
    color: var(--amber); font-weight: 700; font-size: 44px;
    text-transform: uppercase; letter-spacing: 1px; margin-bottom: 20px;
  }
  .contact__line {
    display: flex; align-items: center; gap: 16px;
    color: var(--ink); font-size: 30px; line-height: 1.55;
  }
  .contact__icon { width: 26px; height: 26px; flex: none; }
  .card__footer {
    position: absolute; left: 0; bottom: 0; width: 100%; height: 70px;
    background: var(--charcoal-deep);
    display: flex; align-items: center; padding-left: 60px;
  }
  .address {
    color: var(--amber); font-weight: 700; font-size: 24px;
    text-transform: uppercase; letter-spacing: 1px;
  }
</style>
</head>
<body>
  <main class="card">
    <header class="card__header">
      <div class="brand">
        <span class="brand__disc"></span>
        <span class="brand__name">The Brava Group</span>
      </div>
    </header>

    <section class="card__body">
      <div class="scenery" role="img" aria-label="Illustration: silhouette of a howling wolf on a hilltop"></div>

      <div class="contact">
        <h1 class="contact__name">Martin Hale</h1>
        <p class="contact__line">
          <svg class="contact__icon" viewBox="0 0 26 26" aria-hidden="true"><circle cx="13" cy="13" r="13" fill="var(--amber)"/><path d="M8 7c1-1 2-1 3 1l1 2c0 1-1 1-1 2 1 2 2 3 4 4 1 0 1-1 2-1l2 1c2 1 2 2 1 3-2 2-5 1-8-2s-5-7-4-10z" fill="#fff"/></svg>
          516.555.0143
        </p>
        <p class="contact__line">
          <svg class="contact__icon" viewBox="0 0 26 26" aria-hidden="true"><circle cx="13" cy="13" r="13" fill="var(--amber)"/><rect x="9" y="6" width="8" height="14" rx="1.5" fill="#fff"/><rect x="10.5" y="8" width="5" height="8" fill="var(--amber)"/></svg>
          516.555.0178
        </p>
        <p class="contact__line">
          <svg class="contact__icon" viewBox="0 0 26 26" aria-hidden="true"><circle cx="13" cy="13" r="13" fill="var(--amber)"/><rect x="6" y="8" width="14" height="10" rx="1" fill="#fff"/><path d="M6 8l7 6 7-6" fill="none" stroke="var(--amber)" stroke-width="1.5"/></svg>
          martin@bravagroup-example.com
        </p>
      </div>
    </section>

    <footer class="card__footer">
      <p class="address">12 Cobalt Lane Roslyn New York 11492</p>
    </footer>
  </main>
</body>
</html>
```